Business Card Design

I require the design of business cards using my exisiting logo.

It is essential that the designer has experience with various print processes (foil stamping etc) and different paper stock.

The design is to blend in with current packaging and display unit. (Images will be provided).
A swing tag and certificate of authenticity design will als be required at a later stage.

Details which need to be included on the card are:
- Contact Name
- Position in Company
- Address
- Contact Number
- Email Address
- Web Address

Ideally I would prefer the background (both sides) to be greyish colour (offset printing or if you can suggest greyish paperstock) with silver foiling on the front and either black or metallic silver on the back.

Or another option would be grey background on the front and either white or black on the the back.

* The business card can be portrait or landscape.

Printers specifications:
Bleed 3mm
Trim Marks
Seperate file for foil printing

This task is for someone who is creative and enjoys working with fashion and luxury items!
_______________________________________________

I will require business cards designs for 2 different business and would hope to work with the same designer.

Please note I had asked for a grey colour at least on one of the sides. However I keep on getting black and white designs.   

Business

• - Double sided business card
- Luxury feel
- Foil Print Priniting

- Would prefer at least grey background at least on one side of the card.

- The business card can be portrait or landscape.
• *The business card can be portrait or landscape.
• - Bright Colours
- Alterations to logo

```html
<!DOCTYPE html>
<html lang="en">
<head>
<meta charset="utf-8">
<title>Orin Jewels — Business Card</title>
<link rel="stylesheet" href="https://fonts.googleapis.com/css2?family=Work+Sans:wght@200;300;400&display=swap">
<style>
  :root {
    --canvas-bg: #e9e7e4;
    --card-grey: #434b53;
    --foil-silver: #d9dde1;
    --card-white: #f1f2f4;
    --ink: #1e2226;
    --rule: #2a2e33;
    --shadow: rgba(0, 0, 0, 0.18);
  }
  * { box-sizing: border-box; margin: 0; padding: 0; }
  html, body {
    width: 1200px;
    height: 880px;
    overflow: hidden;
  }
  body {
    background: var(--canvas-bg);
    font-family: "Work Sans", "Helvetica Neue", Arial, sans-serif;
    display: flex;
    align-items: center;
    justify-content: center;
    gap: 40px;
  }
  .card {
    width: 540px;
    height: 309px;
    position: relative;
    flex: none;
    box-shadow: 0 10px 28px var(--shadow);
  }

  /* Front: grey stock, silver foil */
  .card-front {
    background: var(--card-grey);
    display: flex;
    align-items: center;
    justify-content: center;
    gap: 34px;
  }
  .brand-name {
    color: var(--foil-silver);
    font-weight: 200;
    font-size: 44px;
    letter-spacing: 0.02em;
    line-height: 1;
    white-space: nowrap;
  }
  .brand-mark {
    width: 96px;
    height: 96px;
    flex: none;
  }

  /* Back: white stock, black print */
  .card-back {
    background: var(--card-white);
    color: var(--ink);
  }
  .person {
    position: absolute;
    left: 52px;
    top: 100px;
    display: flex;
    align-items: baseline;
    gap: 24px;
    white-space: nowrap;
  }
  .person-name {
    font-weight: 200;
    font-size: 42px;
    letter-spacing: 0.01em;
    line-height: 1;
  }
  .person-role {
    font-weight: 300;
    font-size: 15px;
  }
  .contact-band {
    position: absolute;
    left: 0;
    right: 0;
    bottom: 18px;
    border-top: 1.5px solid var(--rule);
    border-bottom: 1.5px solid var(--rule);
    padding: 11px 20px;
    display: flex;
    align-items: center;
    justify-content: space-between;
    font-weight: 300;
    font-size: 14px;
    line-height: 1.2;
    white-space: nowrap;
  }
  .contact-dot {
    width: 7px;
    height: 7px;
    border: 1.5px solid var(--ink);
    border-radius: 50%;
    flex: none;
  }
</style>
</head>
<body>
  <section class="card card-front" aria-label="Card front">
    <span class="brand-name">ORIN JEWELS</span>
    <svg class="brand-mark" viewBox="0 0 96 96" aria-hidden="true">
      <circle cx="48" cy="48" r="44" fill="none" stroke="var(--foil-silver)" stroke-width="2"/>
    </svg>
  </section>

  <section class="card card-back" aria-label="Card back">
    <div class="person">
      <span class="person-name">MARCUS VALE</span>
      <span class="person-role">| manager</span>
    </div>
    <div class="contact-band">
      <span class="contact-phone">0912-45-6830</span>
      <span class="contact-dot"></span>
      <span class="contact-email">office@orin-jewelry.com</span>
      <span class="contact-dot"></span>
      <span class="contact-web">www.orin-jewelry.com</span>
    </div>
  </section>
</body>
</html>
```